Business card representing 2 natural foods companies!

Would love a business card that represents the 2 companies that I manage, PressVia and Tamberly Crisp Leaf Co. Clearly, they are both premium food brands that have a cool, modern but classic feel.
I'm open to ideas for how to represent on 1 business card that I am Founder and President of both companies.
Contact Information for Business Card
Logos for both brands, and I think the most important thing is 2 different websites for each company (and perhaps 2 different emails for both companies)
sippressvia.com
mort@sippressvia.com
tamberlycrisp.co
mort@tamberlycrisp.co
Address isn't needed. I think phone number is good:
just cell: 555-874-3190
Also thinking is it possible to include a black ProLinka QR code? I think that would be really cool to include.
Look and feel

```html
<!DOCTYPE html>
<html lang="en">
<head>
<meta charset="utf-8">
<title>PressVia &amp; Tamberly Crisp Leaf Co. Business Card</title>
<link href="https://fonts.googleapis.com/css2?family=Oswald:wght@500;700&family=Roboto:wght@400;500&display=swap" rel="stylesheet">
<style>
  :root {
    --stage: #1d1d1d;
    --card-dark: #0b0b0d;
    --card-light: #ffffff;
    --ink: #222222;
    --ink-soft: #444444;
    --paper-text: #ffffff;
    --rule: #333333;
    --code-fill: #111111;
  }
  * { margin: 0; padding: 0; box-sizing: border-box; }
  html, body { width: 1200px; height: 895px; overflow: hidden; }
  body { background: var(--stage); position: relative; font-family: "Roboto", Arial, sans-serif; }

  .card {
    position: absolute;
    width: 640px;
    height: 366px;
    left: 280px;
    box-shadow: 0 10px 30px rgba(0,0,0,0.5);
  }
  .card--front { top: 60px; background: var(--card-dark); color: var(--paper-text); }
  .card--back { top: 469px; background: var(--card-light); color: var(--ink); }

  /* Front */
  .front-brand {
    position: absolute;
    top: 110px; left: 0; right: 0;
    text-align: center;
    font-family: "Oswald", Arial, sans-serif;
    font-weight: 700;
    font-size: 74px;
    letter-spacing: 4px;
    text-transform: uppercase;
    line-height: 1;
  }
  .front-name {
    position: absolute;
    top: 212px; left: 0; right: 0;
    text-align: center;
    font-family: "Oswald", Arial, sans-serif;
    font-weight: 700;
    font-size: 24px;
    letter-spacing: 1px;
    line-height: 1;
  }
  .front-title {
    position: absolute;
    top: 242px; left: 0; right: 0;
    text-align: center;
    font-size: 14px;
    letter-spacing: 0.5px;
  }

  /* Back */
  .back-brand {
    position: absolute;
    top: 38px; right: 38px;
    display: flex; align-items: center; gap: 10px;
    font-family: "Oswald", Arial, sans-serif;
    font-weight: 700;
    font-size: 20px;
    text-transform: uppercase;
    color: var(--ink-soft);
    letter-spacing: 0.5px;
  }
  .back-brand__dot {
    width: 18px; height: 18px; border-radius: 50%;
    border: 2px solid var(--ink-soft);
  }
  .back-rule {
    position: absolute;
    top: 112px; left: 150px; right: 38px;
    height: 1px; background: var(--rule);
  }
  .contact-list {
    list-style: none;
    font-size: 15px;
    line-height: 1.45;
  }
  .contact-list li { display: flex; align-items: center; gap: 10px; }
  .contact-list svg { width: 12px; height: 12px; flex: none; }
  .contact-list--pressvia {
    position: absolute;
    top: 130px; left: 402px;
  }
  .contact-list__label {
    font-family: "Oswald", Arial, sans-serif;
    font-weight: 500;
    font-size: 13px;
    letter-spacing: 1px;
    text-transform: uppercase;
    color: var(--ink-soft);
  }
  .contact-list--main {
    position: absolute;
    top: 280px; left: 46px;
  }
  .back-name {
    position: absolute;
    top: 208px; left: 44px;
    font-family: "Oswald", Arial, sans-serif;
    font-weight: 700;
    font-size: 28px;
    letter-spacing: 0.5px;
    line-height: 1;
  }
  .back-title {
    position: absolute;
    top: 242px; left: 46px;
    font-size: 14px;
  }
  .back-divider {
    position: absolute;
    top: 268px; left: 44px;
    width: 230px; height: 1px; background: var(--rule);
  }
  .profile-code {
    position: absolute;
    right: 38px; bottom: 30px;
    width: 84px; height: 84px;
    background: var(--code-fill);
  }
</style>
</head>
<body>
  <section class="card card--front">
    <div class="front-brand">PressVia</div>
    <div class="front-name">DALE ROURKE</div>
    <div class="front-title">Founder &amp; President</div>
  </section>

  <section class="card card--back">
    <div class="back-brand"><span class="back-brand__dot"></span>Tamberly Crisp Leaf Co.</div>
    <div class="back-rule"></div>

    <ul class="contact-list contact-list--pressvia">
      <li class="contact-list__label">PressVia</li>
      <li>
        <svg viewBox="0 0 24 24" aria-hidden="true"><circle cx="12" cy="12" r="9" fill="none" stroke="#222" stroke-width="2"/><path d="M3 12h18M12 3c3 3 3 15 0 18M12 3c-3 3-3 15 0 18" fill="none" stroke="#222" stroke-width="2"/></svg>
        sippressvia.com
      </li>
      <li>
        <svg viewBox="0 0 24 24" aria-hidden="true"><rect x="2" y="5" width="20" height="14" fill="#222"/><path d="M2 5l10 7 10-7" fill="none" stroke="#fff" stroke-width="2"/></svg>
        mort@sippressvia.com
      </li>
    </ul>

    <div class="back-name">DALE ROURKE</div>
    <div class="back-title">Founder &amp; President</div>
    <div class="back-divider"></div>
    <ul class="contact-list contact-list--main">
      <li>
        <svg viewBox="0 0 24 24" aria-hidden="true"><path fill="#222" d="M6.6 10.8a15.1 15.1 0 0 0 6.6 6.6l2.2-2.2c.3-.3.7-.4 1-.2 1.1.4 2.3.6 3.6.6.6 0 1 .4 1 1V20c0 .6-.4 1-1 1A17 17 0 0 1 3 4c0-.6.4-1 1-1h3.5c.6 0 1 .4 1 1 0 1.3.2 2.5.6 3.6.1.3 0 .7-.2 1z"/></svg>
        555-874-3190
      </li>
      <li>
        <svg viewBox="0 0 24 24" aria-hidden="true"><rect x="2" y="5" width="20" height="14" fill="#222"/><path d="M2 5l10 7 10-7" fill="none" stroke="#fff" stroke-width="2"/></svg>
        mort@tamberlycrisp.co
      </li>
      <li>
        <svg viewBox="0 0 24 24" aria-hidden="true"><circle cx="12" cy="12" r="9" fill="none" stroke="#222" stroke-width="2"/><path d="M3 12h18M12 3c3 3 3 15 0 18M12 3c-3 3-3 15 0 18" fill="none" stroke="#222" stroke-width="2"/></svg>
        tamberlycrisp.co
      </li>
    </ul>

    <div class="profile-code" role="img" aria-label="Space for a black ProLinka profile QR code"></div>
  </section>
</body>
</html>
```